For Lease sign for Property management company in Kansas City

We need someone to take our information and design a standard for lease sign that we can put in front of each of our buildings. I would love for it to do its job of letting people know there are units available but also be unique somehow. Also the aspect ratio of the design would ideally be 4 wide by 3 tall but we open to other ideas. It will be a larger yard sign.

Target Market(s)

Potential Tenants

Industry/Entity Type

Real Estate Development

Font styles to use
Sans Serif

Requirements
Must have
• Our logo, our website (www.quillstead-properties.com), our phone number (816) 555-2719.
Nice to have
• Some how say "For Lease"
Sign to be 4' wide by 3' tall
If there was a place to put the building name that would be cool but not ne
Should not have
• Nothing that I can think of

```html
<!DOCTYPE html>
<html lang="en">
<head>
<meta charset="utf-8">
<title>For Lease Yard Sign – Quillstead Properties</title>
<link href="https://fonts.googleapis.com/css2?family=Archivo+Black&family=Roboto:wght@400;700;900&display=swap" rel="stylesheet">
<style>
  :root {
    --crimson: #c41e3a;
    --orange: #f7a21b;
    --white: #ffffff;
    --ink: #1a1a1a;
    --backdrop: #ececec;
  }
  * { margin: 0; padding: 0; box-sizing: border-box; }
  html, body {
    width: 729px;
    height: 1200px;
    overflow: hidden;
    background: var(--backdrop);
  }
  .canvas {
    position: relative;
    width: 729px;
    height: 1200px;
  }
  .sign {
    position: absolute;
    left: 34px;
    top: 352px;
    width: 660px;
    height: 495px;
    background: var(--white);
    overflow: hidden;
    box-shadow: 0 6px 18px rgba(0,0,0,0.18);
  }
  .sign__bands {
    position: absolute;
    inset: 0;
    width: 100%;
    height: 100%;
  }
  .headline {
    position: absolute;
    left: 120px;
    top: 36px;
    width: 420px;
    height: 64px;
    border-radius: 32px;
    background: var(--orange);
    display: flex;
    align-items: center;
    justify-content: center;
    font-family: "Archivo Black", "Arial Black", sans-serif;
    font-size: 44px;
    letter-spacing: 1px;
    color: var(--ink);
  }
  .phone {
    position: absolute;
    left: 0;
    top: 120px;
    width: 100%;
    text-align: center;
    font-family: "Roboto", Arial, sans-serif;
    font-weight: 700;
    font-size: 44px;
    letter-spacing: 1px;
    color: var(--white);
  }
  .website {
    position: absolute;
    left: 0;
    top: 178px;
    width: 100%;
    text-align: center;
    font-family: "Roboto", Arial, sans-serif;
    font-weight: 700;
    font-size: 22px;
    color: var(--white);
  }
  .building-name {
    position: absolute;
    left: 190px;
    top: 222px;
    width: 280px;
    height: 34px;
    border-radius: 17px;
    background: var(--white);
    display: flex;
    align-items: center;
    justify-content: center;
    font-family: "Roboto", Arial, sans-serif;
    font-weight: 400;
    font-size: 19px;
    letter-spacing: 1px;
    color: var(--ink);
  }
  .brand {
    position: absolute;
    left: 150px;
    top: 350px;
    display: flex;
    align-items: center;
    gap: 18px;
  }
  .brand__dot {
    width: 92px;
    height: 92px;
    border-radius: 50%;
    background: var(--orange);
    flex: none;
  }
  .brand__name {
    font-family: "Roboto", Arial, sans-serif;
    font-weight: 900;
    font-size: 38px;
    line-height: 1.05;
    color: var(--crimson);
    letter-spacing: 1px;
  }
</style>
</head>
<body>
<main class="canvas">
  <section class="sign" aria-label="For lease yard sign">
    <svg class="sign__bands" viewBox="0 0 660 495" preserveAspectRatio="none" aria-hidden="true">
      <path d="M0 0 H660 V250 C500 300 260 320 0 300 Z" fill="var(--orange)"/>
      <path d="M0 0 H660 V236 C500 282 260 298 0 282 Z" fill="var(--crimson)"/>
    </svg>
    <div class="headline">FOR LEASE</div>
    <div class="phone">(816) 555-2719</div>
    <div class="website">www.quillstead-properties.com</div>
    <div class="building-name">BUILDING NAME</div>
    <div class="brand">
      <span class="brand__dot" aria-hidden="true"></span>
      <span class="brand__name">QUILLSTEAD<br>PROPERTIES</span>
    </div>
  </section>
</main>
</body>
</html>
```